Business Card / Appointment Card for Physician

On one side it should give the logo, address, and contact information, and on the other side it should br an Appointment card.

One Side:
Logo (see attached files)
Board Certified American Orthopedic Surgery

1874 Larkmoor Ave.
Suite KP7
Bronx, NY 10287
Tel: (718) 555 - 0142
Fax: (718) 555 - 0187

612 Ninth Ave.
Suite 42
New York, NY 10089
Tel: (212) 555 - 0163

Second Side:
Appointment
give them a choice of Bronx or Mahattan office
For:
Date:
Time:

If you are unable to keep your appointment, please call (718) 555-0129 24hrs in advance.

Target Market(s)

People that need orthopedic surgery

Industry/Entity Type

Business

Contact Information for Business Card

smart and attractive

Requirements
Must have
• logo
• contact information on one side, appointment information on the other

```html
<!DOCTYPE html>
<html lang="en">
<head>
<meta charset="utf-8">
<title>Appointment and Contact Cards</title>
<link href="https://fonts.googleapis.com/css2?family=Source+Sans+3:ital,wght@0,300;0,400;0,600;0,700;1,300&display=swap" rel="stylesheet">
<style>
  :root {
    --green: #5fa443;
    --blue: #1f5f98;
    --navy: #2a6496;
    --pattern: #ececef;
    --paper: #ffffff;
    --stage: #e4e6ea;
    --ink: #222;
  }
  * { box-sizing: border-box; margin: 0; padding: 0; }
  html, body { width: 1200px; height: 863px; overflow: hidden; }
  body {
    background: var(--stage);
    font-family: "Source Sans 3", "Myriad Pro", Arial, sans-serif;
    display: flex; align-items: center; justify-content: center; gap: 60px;
  }
  .card {
    position: relative; width: 300px; height: 525px;
    background: var(--paper); overflow: hidden;
    box-shadow: 0 6px 18px rgba(0,0,0,.12);
  }
  .card__base {
    position: absolute; left: 0; right: 0; bottom: 0; height: 150px;
  }
  .card__arch {
    position: absolute; left: -40px; right: -40px; bottom: 50px; height: 260px;
    background: var(--paper); border-radius: 0 0 50% 50% / 0 0 100% 100%;
  }
  .card__pattern {
    position: absolute; background: var(--pattern);
  }
  .card__content { position: relative; z-index: 2; }

  /* Appointment side */
  .appointment .card__base { background: var(--green); }
  .appointment .card__pattern {
    left: 20px; right: 20px; top: 0; bottom: 60px;
    border-radius: 0 0 50% 50% / 0 0 30% 30%;
  }
  .appointment__title {
    text-align: right; padding: 60px 26px 0 0;
    color: var(--green); font-weight: 700; font-size: 34px;
  }
  .office-choice {
    display: flex; justify-content: space-between; padding: 16px 26px 0 36px;
    color: var(--blue); font-weight: 600; font-size: 15px;
  }
  .office-choice span { display: flex; align-items: center; gap: 6px; }
  .checkbox { width: 16px; height: 16px; border: 1.5px solid #333; background: #fff; }
  .fields { padding: 30px 26px 0 36px; }
  .field {
    display: flex; align-items: flex-end; gap: 8px; margin-bottom: 18px;
    color: var(--blue); font-weight: 600; font-size: 15px;
  }
  .field__line { flex: 1; border-bottom: 1.5px solid #333; height: 14px; }
  .notice {
    text-align: center; font-size: 14px; line-height: 1.25;
    color: var(--ink); padding: 34px 30px 0;
  }

  /* Contact side */
  .contact .card__base { background: var(--navy); }
  .contact .card__pattern {
    left: 0; right: 0; top: 175px; bottom: 60px;
    border-radius: 0 0 50% 50% / 0 0 25% 25%;
  }
  .brand {
    display: flex; align-items: center; justify-content: center; gap: 8px;
    padding: 60px 14px 0; color: var(--blue);
    font-weight: 400; font-size: 19px; letter-spacing: .3px;
  }
  .brand__mark { width: 18px; height: 18px; border-radius: 50%; background: var(--blue); flex: none; }
  .certification {
    margin-top: 44px; background: var(--green); color: #fff;
    font-style: italic; font-weight: 300; font-size: 16px;
    text-align: center; line-height: 1.2; padding: 10px 0;
  }
  .office {
    text-align: center; color: var(--blue); font-size: 15px; line-height: 1.2;
  }
  .office:first-of-type { margin-top: 20px; }
  .office + .office { margin-top: 18px; }
  .office svg { display: block; margin: 0 auto 6px; }
  .office .phone { color: var(--green); font-weight: 700; }
</style>
</head>
<body>

<section class="card appointment">
  <div class="card__base"></div>
  <div class="card__arch"></div>
  <div class="card__pattern" role="img" aria-label="Faint line pattern of a knee joint"></div>
  <div class="card__content">
    <h1 class="appointment__title">Appointment</h1>
    <div class="office-choice">
      <span>Bronx <i class="checkbox"></i></span>
      <span>Mahattan <i class="checkbox"></i></span>
    </div>
    <div class="fields">
      <div class="field">FOR <span class="field__line"></span></div>
      <div class="field">Date <span class="field__line"></span></div>
      <div class="field">Time <span class="field__line"></span></div>
    </div>
    <p class="notice">If you are unable to keep<br>your appointment,<br>Please call (718) 555-0129<br>24hrs in advance</p>
  </div>
</section>

<section class="card contact">
  <div class="card__base"></div>
  <div class="card__arch"></div>
  <div class="card__pattern" role="img" aria-label="Faint line pattern of a knee joint"></div>
  <div class="card__content">
    <div class="brand"><span class="brand__mark"></span>DANIEL R. WHITCOMBE MD PC</div>
    <p class="certification">Board Certified<br>American Orthopedic Surgery</p>
    <address class="office">
      <svg width="20" height="16" viewBox="0 0 20 16" aria-hidden="true"><path d="M10 0 L20 8 H17 V16 H12 V11 H8 V16 H3 V8 H0 Z" fill="#5fa443"/></svg>
      1874 Larkmoor Ave.<br>Suite KP7<br>Bronx, NY 10287<br>
      <span class="phone">Tel: (718) 555 - 0142</span><br>Fax: (718) 555 - 0187
    </address>
    <address class="office">
      <svg width="20" height="16" viewBox="0 0 20 16" aria-hidden="true"><path d="M10 0 L20 8 H17 V16 H12 V11 H8 V16 H3 V8 H0 Z" fill="#5fa443"/></svg>
      612 Ninth Ave.<br>Suite 42<br>New York, NY 10089<br>
      <span class="phone">Tel: (212) 555 - 0163</span>
    </address>
  </div>
</section>

</body>
</html>
```